Crestline Pools New website

I currently operate a swimming pool service and repair business and looking for a re design for my website as it has been over 5 years since it was designed. current site is crestlinepoolsqv.com

```html
<!DOCTYPE html>
<html lang="en">
<head>
<meta charset="utf-8">
<title>Crestline Pools</title>
<link href="https://fonts.googleapis.com/css2?family=Playfair+Display:wght@700;800&family=Poppins:wght@400;500;600;700&display=swap" rel="stylesheet">
<style>
:root{
  --navy:#0b2b6c;
  --blue:#0c5a9e;
  --sky:#36b4e8;
  --orange:#f7941d;
  --gold:#f5b400;
  --white:#ffffff;
  --ink:#3a3a3a;
  --backdrop:#cfcfcf;
}
*{box-sizing:border-box;margin:0;padding:0}
html,body{width:1200px;height:2445px;overflow:hidden;background:var(--backdrop)}
.site{position:absolute;left:81px;top:81px;width:1093px;height:2405px;transform:scale(.9494);transform-origin:0 0;background:var(--navy);box-shadow:0 6px 18px rgba(0,0,0,.25);overflow:hidden;font-family:'Poppins',sans-serif;color:var(--white)}
.abs{position:absolute}
.serif{font-family:'Playfair Display',serif}
.center{text-align:center}

.hero-corner{left:0;top:0}
.brand{left:150px;top:82px;width:245px;display:flex;align-items:center;gap:10px;justify-content:center}
.brand-dot{width:22px;height:22px;border-radius:50%;background:var(--orange)}
.brand-name{font-family:'Playfair Display',serif;font-weight:700;font-size:26px;color:var(--white)}

.nav{right:25px;top:14px;display:flex;gap:26px;font-weight:600;font-size:13px}
.nav a{color:var(--white);text-decoration:none;position:relative;padding-bottom:6px}
.nav a.active::after{content:"";position:absolute;left:0;right:0;bottom:-4px;height:3px;background:var(--orange)}

.hero-title{left:40px;top:218px;width:465px;font-weight:800;font-size:44px;line-height:51px}
.hero-sub{left:40px;top:388px;width:465px;font-size:19px;line-height:33px}
.btn{display:inline-block;background:var(--orange);color:var(--white);font-weight:700;text-transform:uppercase;text-align:center}
.hero-btn{left:181px;top:477px;width:180px;height:40px;line-height:40px;font-size:16px;border-radius:2px}
.hero-photo{left:0;top:0}

.circle-title{left:0;width:1093px}
.bubble{position:absolute;width:50px;height:50px;margin:-25px 0 0 -25px;border-radius:50%;background:var(--blue);border:2.5px solid var(--gold);font-family:'Playfair Display',serif;font-weight:700;font-size:38px;line-height:44px;text-align:center;color:var(--white)}

.resort-photo{left:0;top:790px;width:1093px;height:740px;background:linear-gradient(180deg,var(--navy) 0%,#1f4f8e 18%,#7aa5c4 40%,#c9d6dc 52%,#3fa6cf 66%,#1b87c0 82%,#2d6aa5 100%)}
.card{position:absolute;top:791px;width:223px;height:255px;background:var(--white);border-radius:6px;text-align:center;color:var(--ink)}
.card svg{position:absolute;left:68px;top:22px}
.card-title{position:absolute;left:0;right:0;top:121px;font-family:'Playfair Display',serif;font-weight:700;font-size:17.5px;color:var(--blue)}
.card-text{position:absolute;left:22px;right:22px;top:150px;font-size:10.3px;line-height:15.6px}
.card-btn{position:absolute;left:70px;top:211px;width:84px;height:22px;line-height:22px;font-size:9px;border-radius:2px}

.about-title{left:0;width:1093px;top:1275px;font-size:40px;text-shadow:0 2px 6px rgba(0,0,0,.35)}
.about-text{left:250px;width:593px;top:1325px;font-size:10.3px;line-height:16.8px;text-shadow:0 1px 3px rgba(0,0,0,.4)}
.about-btn{left:505px;top:1427px;width:84px;height:22px;line-height:22px;font-size:9px;border-radius:2px}

.cta{left:0;top:1530px;width:1093px;height:245px;background:linear-gradient(180deg,#f79a24,#f58f14)}
.cta-title{left:0;width:1093px;top:1563px;font-size:45px}
.cta-sub{left:0;width:1093px;top:1627px;font-size:24.5px}
.cta-btn{left:429px;top:1679px;width:235px;height:51px;line-height:51px;background:var(--blue);font-weight:700;font-size:21px;border-radius:2px;color:var(--white)}

.contact-sub{left:0;width:1093px;top:1964px;font-size:16.5px;line-height:22px}
.form{left:174px;top:2037px;width:352px;height:251px;background:var(--white);border-radius:10px}
.field{position:absolute;left:19px;width:315px;height:28px;border:1px solid #d6d6d6;border-radius:3px;font-size:8px;color:#999;padding:9px 7px}
.send{position:absolute;left:19px;top:210px;width:91px;height:23px;line-height:23px;border-radius:12px;font-size:8.5px;text-transform:none}
.touch-title{left:567px;top:2095px;font-size:26px;color:var(--orange)}
.touch-item{left:567px;display:flex;align-items:center;gap:8px;font-size:14.5px}
.touch-icon{width:24px;height:24px;border-radius:50%;border:1.5px solid var(--orange);background:var(--blue);display:flex;align-items:center;justify-content:center}

.footer{left:0;top:2365px;width:1093px;height:40px;background:var(--white);color:#555;font-size:9.5px;line-height:40px}
</style>
</head>
<body>
<div class="site">

  <svg class="abs hero-corner" width="260" height="140" viewBox="0 0 260 140" aria-hidden="true">
    <polygon points="0,0 175,0 0,92" fill="var(--sky)"/>
    <polygon points="175,0 188,0 0,110 0,92" fill="var(--blue)"/>
    <line x1="0" y1="118" x2="200" y2="0" stroke="var(--orange)" stroke-width="5"/>
  </svg>

  <div class="abs brand"><span class="brand-dot"></span><span class="brand-name">Crestline Pools</span></div>

  <nav class="abs nav">
    <a class="active" href="#">Home</a><a href="#">About Us</a><a href="#">Our Services</a><a href="#">Free Estimate</a><a href="#">Contact</a>
  </nav>

  <h1 class="abs hero-title serif center">CRYSTAL<br>CLEAR POOLS, ALL<br>YEAR ROUND</h1>
  <p class="abs hero-sub center">Your trusted partner for pool maintenance,<br>repair &amp; remodeling in Quarry Vale.</p>
  <a class="abs btn hero-btn">Get a Free Quote</a>

  <svg class="abs hero-photo" width="1093" height="700" viewBox="0 0 1093 700">
    <defs>
      <linearGradient id="villa" x1="0" y1="0" x2="0" y2="1">
        <stop offset="0" stop-color="#8a8f84"/>
        <stop offset=".35" stop-color="#a88a64"/>
        <stop offset=".6" stop-color="#3f6a58"/>
        <stop offset=".8" stop-color="#6d7f6a"/>
        <stop offset="1" stop-color="#b7a287"/>
      </linearGradient>
    </defs>
    <polygon points="515,362 955,80 1400,362 955,645" fill="none" stroke="var(--gold)" stroke-width="34" stroke-linejoin="round"/>
    <polygon points="515,362 955,80 1400,362 955,645" fill="none" stroke="var(--blue)" stroke-width="22" stroke-linejoin="round"/>
    <polygon points="540,362 955,96 1380,362 955,628" fill="url(#villa)" stroke="url(#villa)" stroke-width="12" stroke-linejoin="round" role="img" aria-label="Photo of a luxury villa with a landscaped pool and palm trees"/>
  </svg>

  <div class="abs resort-photo" role="img" aria-label="Photo of a resort pool lined with white gazebos and palm trees"></div>

  <div class="abs circle-title" style="top:0">
    <span class="bubble" style="left:502px;top:682px">O</span>
    <span class="bubble" style="left:548px;top:682px">U</span>
    <span class="bubble" style="left:593px;top:682px">R</span>
    <span class="bubble" style="left:409px;top:733px">S</span>
    <span class="bubble" style="left:455px;top:733px">E</span>
    <span class="bubble" style="left:501px;top:733px">V</span>
    <span class="bubble" style="left:547px;top:733px">I</span>
    <span class="bubble" style="left:593px;top:733px">C</span>
    <span class="bubble" style="left:640px;top:733px">E</span>
    <span class="bubble" style="left:686px;top:733px">S</span>
  </div>

  <div class="card" style="left:61px">
    <svg width="88" height="88" viewBox="0 0 88 88" role="img" aria-label="Pool cleaning icon"><polygon points="44,3 85,44 44,85 3,44" fill="var(--white)" stroke="var(--gold)" stroke-width="3" stroke-linejoin="round"/><polygon points="44,8 80,44 44,80 8,44" fill="none" stroke="var(--blue)" stroke-width="3" stroke-linejoin="round"/><circle cx="44" cy="44" r="14" fill="var(--blue)"/></svg>
    <div class="card-title">Pool Cleaning</div>
    <div class="card-text">Regular cleaning to keep your pool sparkling clean &amp; hygienic for your family and friends.</div>
    <a class="btn card-btn">Learn More</a>
  </div>
  <div class="card" style="left:311px">
    <svg width="88" height="88" viewBox="0 0 88 88" role="img" aria-label="Repairs icon"><polygon points="44,3 85,44 44,85 3,44" fill="var(--white)" stroke="var(--gold)" stroke-width="3" stroke-linejoin="round"/><polygon points="44,8 80,44 44,80 8,44" fill="none" stroke="var(--blue)" stroke-width="3" stroke-linejoin="round"/><circle cx="44" cy="44" r="14" fill="var(--blue)"/></svg>
    <div class="card-title">Repairs &amp; Equipment</div>
    <div class="card-text">From leak detection to pump &amp; filter repairs, our technicians fix issues promptly &amp; professionally.</div>
    <a class="btn card-btn">Learn More</a>
  </div>
  <div class="card" style="left:560px">
    <svg width="88" height="88" viewBox="0 0 88 88" role="img" aria-label="Maintenance plans icon"><polygon points="44,3 85,44 44,85 3,44" fill="var(--white)" stroke="var(--gold)" stroke-width="3" stroke-linejoin="round"/><polygon points="44,8 80,44 44,80 8,44" fill="none" stroke="var(--blue)" stroke-width="3" stroke-linejoin="round"/><circle cx="44" cy="44" r="14" fill="var(--blue)"/></svg>
    <div class="card-title">Maintenance Plans</div>
    <div class="card-text">Custom maintenance plans tailored to your needs for worry‑free pool ownership.</div>
    <a class="btn card-btn">Learn More</a>
  </div>
  <div class="card" style="left:808px">
    <svg width="88" height="88" viewBox="0 0 88 88" role="img" aria-label="Renovation icon"><polygon points="44,3 85,44 44,85 3,44" fill="var(--white)" stroke="var(--gold)" stroke-width="3" stroke-linejoin="round"/><polygon points="44,8 80,44 44,80 8,44" fill="none" stroke="var(--blue)" stroke-width="3" stroke-linejoin="round"/><circle cx="44" cy="44" r="14" fill="var(--blue)"/></svg>
    <div class="card-title">Renovation &amp; Remodel</div>
    <div class="card-text">Transform your backyard with custom pool resurfacing, tile work &amp; modern upgrades.</div>
    <a class="btn card-btn">Learn More</a>
  </div>

  <h2 class="abs about-title serif center">About Crestline Pools QV</h2>
  <p class="abs about-text center">Crestline Pools QV is a family‑owned and operated pool service and repair company serving Quarry Vale and surrounding areas. With over a decade of experience, we are dedicated to providing reliable, top‑quality pool care so you can enjoy your backyard oasis year round. We take pride in our attention to detail, friendly customer service, and deep knowledge of pool systems. Whether you need weekly cleaning, urgent repairs or a complete pool renovation, our certified technicians are here to help.</p>
  <a class="abs btn about-btn">Learn More</a>

  <div class="abs cta"></div>
  <h2 class="abs cta-title serif center">Relax, We’ve Got Your Pool Covered</h2>
  <p class="abs cta-sub center">Let our experts keep your pool safe, clean &amp; ready for every occasion.</p>
  <a class="abs cta-btn center">Schedule Service</a>

  <div class="abs circle-title" style="top:0">
    <span class="bubble" style="left:406px;top:1883px">C</span>
    <span class="bubble" style="left:452px;top:1883px">O</span>
    <span class="bubble" style="left:499px;top:1883px">N</span>
    <span class="bubble" style="left:546px;top:1883px">T</span>
    <span class="bubble" style="left:593px;top:1883px">A</span>
    <span class="bubble" style="left:640px;top:1883px">C</span>
    <span class="bubble" style="left:686px;top:1883px">T</span>
    <span class="bubble" style="left:523px;top:1930px">U</span>
    <span class="bubble" style="left:570px;top:1930px">S</span>
  </div>
  <p class="abs contact-sub center">Ready to make a splash? Send us a message or give us a call<br>and we’ll get back to you as soon as possible.</p>

  <form class="abs form">
    <div class="field" style="top:18px">Your Name</div>
    <div class="field" style="top:55px">Email Address</div>
    <div class="field" style="top:93px">Phone Number</div>
    <div class="field" style="top:130px;height:67px">How can we help you?</div>
    <span class="btn send">Send Message</span>
  </form>

  <h3 class="abs touch-title serif">Get in Touch</h3>
  <div class="abs touch-item" style="top:2137px">
    <span class="touch-icon"><svg width="12" height="12" viewBox="0 0 24 24"><path d="M6 2h4l2 5-3 2a12 12 0 006 6l2-3 5 2v4a2 2 0 01-2 2A19 19 0 014 4a2 2 0 012-2z" fill="var(--white)"/></svg></span>(555) 014-2290</div>
  <div class="abs touch-item" style="top:2166px">
    <span class="touch-icon"><svg width="12" height="12" viewBox="0 0 24 24"><rect x="2" y="5" width="20" height="14" rx="2" fill="none" stroke="var(--white)" stroke-width="2"/><path d="M2 6l10 7 10-7" fill="none" stroke="var(--white)" stroke-width="2"/></svg></span>info@crestlinepoolsqv.com</div>
  <div class="abs touch-item" style="top:2195px">
    <span class="touch-icon"><svg width="12" height="12" viewBox="0 0 24 24"><path d="M12 2a7 7 0 017 7c0 5-7 13-7 13S5 14 5 9a7 7 0 017-7z" fill="var(--white)"/><circle cx="12" cy="9" r="2.5" fill="var(--blue)"/></svg></span>Quarry Vale, QV</div>

  <footer class="abs footer center">© 2026 Crestline Pools QV. All rights reserved.</footer>
</div>
</body>
</html>
```